Need 8.5" x 11" as well as large 11"x17" Posters for our upcoming event

Please include LOGOs in poster
Main logo is Harborline Teen Circle of WB

All high school age faith groups are invited to come and join with 150 to 175 other high school students from various faith traditions to participate in the Harborline Teen Circle of Westbrook Basin‘s Annual Lanternway Teen Gathering. More than ever, our county and world need young leaders who are willing to learn from each other and build stronger communities!

KINDRED TABLE
The purpose of this Lanternway Teen Gathering is to bring together young people from diverse ethnic, cultural, and religious backgrounds, and to engage them in dialogue. True dialogue is a conversation on a common subject between two or more persons of differing points of view and/or backgrounds. We feel that this commitment to dialogue will affect relationships in a constructive way in our places of worship and in our community.
The forum itself involves having eight religiously diverse high school-age students, one adult, and youth leader around each table to discuss common questions. Our youth leaders act as facilitators, but it is stressed that it is the students we want to hear from.
RSVP for our KINDRED TABLE before February 18th, 2018
FORUM QUESTIONS Available online at http://hltcwb.example/home/kindred-fair/

Target Market(s)

Houses of worship, community leaders, High School Students

Industry/Entity Type

Non-Profit

Font styles to use
Serif

Colors
cfdeed
0255a3
f78f20
f37122
f68d4d
faa54b
ffcf3e
ffc214
34a6d7

Requirements
Must have
• Harborline Teen Circle of Westbrook Basin's 14th Annual Kindred Table & Fair
• TEENS EXPRESSING THEIR FAITH THROUGH ART, MUSIC, AND DIALOGUE
• THIS YEAR'S THEME: “Who Are You?”
• Sunday, March 11th, 2018 11:00am-5:00pm
• Congregation Ner Tamid Hall
• 4810 W Marlow Rd. Santa Ana, CA 92704
• Email: hltcwbteam@mailbox.example
• Website: HLTCWB.example
• Facebook: Harborline Teen Circle of Westbrook Basin
Nice to have
• Descriptions provided in word doc
Should not have
• -

```html
<!DOCTYPE html>
<html lang="en">
<head>
<meta charset="utf-8">
<title>Harborline Teen Circle of Westbrook Basin's 14th Annual Kindred Table &amp; Fair</title>
<link rel="stylesheet" href="https://fonts.googleapis.com/css2?family=Kaushan+Script&family=Montserrat:wght@400;600;700&family=Oswald:wght@500&display=swap">
<style>
  :root {
    --blue-deep: #0255a3;
    --blue-mid: #1f7fd0;
    --blue-sky: #34a6d7;
    --blue-pale: #cfdeed;
    --orange: #f78f20;
    --orange-dark: #f37122;
    --orange-soft: #f68d4d;
    --white: #ffffff;
    --strip: #e8edf2;
  }
  * { margin: 0; padding: 0; box-sizing: border-box; }
  html, body { width: 927px; height: 1200px; overflow: hidden; }
  body { font-family: "Montserrat", sans-serif; color: var(--white); }

  .poster {
    position: relative;
    width: 927px;
    height: 1200px;
    overflow: hidden;
    background: linear-gradient(180deg, var(--blue-deep) 0%, var(--blue-mid) 40%, #4ea2cf 70%, #a89a8e 86%, var(--orange-dark) 100%);
  }

  .hero-photo {
    position: absolute;
    left: 0; top: 0;
    width: 927px; height: 604px;
    background: radial-gradient(ellipse at 45% 55%, rgba(90,160,225,0.55), rgba(20,100,190,0) 65%),
                linear-gradient(180deg, #1a74cc 0%, #3d95da 100%);
  }

  .council-mark {
    position: absolute;
    left: 52px; top: 48px;
    width: 196px; height: 196px;
    display: flex; align-items: center; justify-content: center;
    text-align: center;
  }
  .council-mark svg { position: absolute; inset: 0; }
  .council-mark span {
    position: relative;
    width: 120px;
    font-weight: 700;
    font-size: 15px;
    line-height: 1.25;
    color: var(--white);
  }

  .org-heading {
    position: absolute;
    left: 286px; top: 106px;
    font-weight: 600;
    font-size: 31px;
    line-height: 36px;
    letter-spacing: 1px;
    text-transform: uppercase;
  }

  .event-info {
    position: absolute;
    top: 302px;
    font-family: "Oswald", sans-serif;
    font-weight: 500;
    font-size: 22px;
    line-height: 28px;
    letter-spacing: 1px;
    text-transform: uppercase;
    text-align: center;
  }
  .event-info.venue { left: 36px; width: 260px; }
  .event-info.when { left: 680px; width: 210px; }

  .photo-strip {
    position: absolute;
    left: 0; top: 604px;
    width: 927px; height: 228px;
  }
  .photo-frame {
    position: absolute;
    top: 0;
    height: 228px;
    background: var(--strip);
    box-shadow: 0 2px 6px rgba(0,0,0,0.25);
  }
  .photo-frame .shot {
    position: absolute;
    left: 10px; right: 10px; top: 10px;
    height: 170px;
  }
  .f1 { left: -8px; width: 172px; } .f1 .shot { left: 8px; background: linear-gradient(160deg, #6b86b8, #a9917d); }
  .f2 { left: 170px; width: 190px; } .f2 .shot { background: linear-gradient(170deg, #3b2b24, #9a6a44 60%, #c99a6a); }
  .f3 { left: 368px; width: 190px; } .f3 .shot { background: linear-gradient(160deg, #6b4c3a, #4b3a30 60%, #7a5a48); }
  .f4 { left: 566px; width: 190px; } .f4 .shot { background: linear-gradient(160deg, #e9dcd4, #9e6a52 55%, #5a2f25); }
  .f5 { left: 762px; width: 176px; } .f5 .shot { right: 0; background: linear-gradient(160deg, #d9c7b8, #8a6a5c 55%, #c9b3a4); }

  .event-title {
    position: absolute;
    left: 200px; top: 196px;
    width: 540px; height: 480px;
    font-family: "Kaushan Script", cursive;
    color: var(--white);
    text-align: center;
    z-index: 2;
  }
  .event-title .line {
    position: absolute;
    left: 0; right: 0;
    line-height: 1;
    text-shadow:
      -3px -3px 0 var(--orange), 3px -3px 0 var(--orange), -3px 3px 0 var(--orange), 3px 3px 0 var(--orange),
      5px 5px 0 var(--orange-dark), 7px 7px 0 var(--orange-dark), 9px 9px 0 #d9761a, 11px 11px 0 #c86a14;
  }
  .t-num { top: 0; font-size: 138px; }
  .t-annual { top: 140px; font-size: 86px; }
  .t-name { top: 232px; font-size: 74px; }
  .t-amp { top: 310px; font-size: 78px; }
  .t-fair { top: 376px; font-size: 104px; }

  .tagline {
    position: absolute;
    left: 0; top: 836px;
    width: 927px;
    font-weight: 600;
    font-size: 31px;
    line-height: 33px;
    text-align: center;
    text-transform: uppercase;
  }

  .theme-ribbon { position: absolute; left: 56px; top: 914px; width: 812px; height: 42px; }
  .theme-ribbon svg { position: absolute; inset: 0; }
  .theme-ribbon p {
    position: absolute;
    left: 0; right: 0; top: 7px;
    text-align: center;
    font-size: 24px;
    letter-spacing: 1px;
    text-transform: uppercase;
  }
  .theme-ribbon strong { font-weight: 700; }

  .invitation {
    position: absolute;
    left: 64px; top: 988px;
    width: 800px;
    font-weight: 700;
    font-size: 14.4px;
    line-height: 18px;
    text-align: center;
  }

  .footer {
    position: absolute;
    left: 56px; top: 1084px;
    width: 818px; height: 68px;
    display: flex; align-items: center; justify-content: space-between;
  }
  .partner-box {
    width: 116px; height: 68px;
    background: var(--white);
    display: flex; align-items: center; justify-content: center;
    text-align: center;
    font-family: "Montserrat", sans-serif;
    font-weight: 600;
    color: var(--blue-deep);
    padding: 6px;
  }
  .partner-box.ally { font-size: 15px; line-height: 1.1; }
  .partner-box.host { font-size: 11px; line-height: 1.2; }
  .contact-list { display: flex; align-items: center; gap: 14px; font-size: 12px; font-weight: 400; }
  .contact-list li { list-style: none; display: flex; align-items: center; gap: 6px; white-space: nowrap; }
  .contact-list svg { flex: none; }
  .square-mark { width: 20px; height: 20px; background: var(--white); display: block; }
</style>
</head>
<body>
<main class="poster">
  <div class="hero-photo" role="img" aria-label="Photo of teenagers jumping joyfully outdoors in winter, tinted blue"></div>

  <div class="council-mark">
    <svg viewBox="0 0 196 196" width="196" height="196" aria-hidden="true">
      <circle cx="98" cy="98" r="92" fill="none" stroke="var(--white)" stroke-width="3"/>
    </svg>
    <span>Harborline Teen Circle of WB</span>
  </div>

  <h2 class="org-heading">Harborline Teen Circle<br>of Westbrook Basin's</h2>

  <p class="event-info venue">Congregation Ner Tamid Hall<br>4810 W Marlow Rd.<br>Santa Ana, CA 92704</p>
  <p class="event-info when">Sunday,<br>March 11th, 2018<br>11:00am–5:00pm</p>

  <section class="photo-strip">
    <div class="photo-frame f1"><div class="shot" role="img" aria-label="Photo of a group of smiling teens in matching t-shirts"></div></div>
    <div class="photo-frame f2"><div class="shot" role="img" aria-label="Photo of dancers performing on a stage"></div></div>
    <div class="photo-frame f3"><div class="shot" role="img" aria-label="Photo of hands creating colorful sand art"></div></div>
    <div class="photo-frame f4"><div class="shot" role="img" aria-label="Photo of teens playing large drums"></div></div>
    <div class="photo-frame f5"><div class="shot" role="img" aria-label="Photo of teens playing music at a microphone"></div></div>
  </section>

  <h1 class="event-title">
    <span class="line t-num">14th</span>
    <span class="line t-annual">Annual</span>
    <span class="line t-name">Kindred Table</span>
    <span class="line t-amp">&amp;</span>
    <span class="line t-fair">Fair</span>
  </h1>

  <p class="tagline">Teens expressing their faith through<br>art, music, and dialogue</p>

  <div class="theme-ribbon">
    <svg viewBox="0 0 812 42" width="812" height="42" aria-hidden="true">
      <polygon points="0,6 100,6 100,40 0,40 22,23" fill="var(--orange-dark)"/>
      <polygon points="812,6 712,6 712,40 812,40 790,23" fill="var(--orange-dark)"/>
      <rect x="92" y="0" width="628" height="36" fill="var(--orange)"/>
    </svg>
    <p>This year's theme: <strong>Who are you?</strong></p>
  </div>

  <p class="invitation">All high school age faith groups are invited to come and join with 150 to 175 other high school students from various faith traditions to participate in the Harborline Teen Circle of Westbrook Basin‘s Annual Lanternway Teen Gathering. More than ever, our county and world need young leaders who are willing to learn from each other and build stronger communities!</p>

  <footer class="footer">
    <div class="partner-box ally">Brightpath Allies</div>
    <ul class="contact-list">
      <li>
        <svg width="22" height="20" viewBox="0 0 22 20" aria-hidden="true"><rect x="1" y="5" width="20" height="14" fill="none" stroke="var(--white)" stroke-width="1.5"/><polyline points="1,5 11,13 21,5" fill="none" stroke="var(--white)" stroke-width="1.5"/></svg>
        hltcwbteam@mailbox.example
      </li>
      <li>
        <svg width="22" height="22" viewBox="0 0 22 22" aria-hidden="true"><circle cx="11" cy="11" r="9.5" fill="none" stroke="var(--white)" stroke-width="1.5"/><ellipse cx="11" cy="11" rx="4" ry="9.5" fill="none" stroke="var(--white)" stroke-width="1.2"/><line x1="1.5" y1="11" x2="20.5" y2="11" stroke="var(--white)" stroke-width="1.2"/></svg>
        HLTCWB.example
      </li>
      <li><span class="square-mark" aria-hidden="true"></span>Harborline Teen Circle of Westbrook Basin</li>
    </ul>
    <div class="partner-box host">Congregation Ner Tamid Hall</div>
  </footer>
</main>
</body>
</html>
```